Business card design for strategy and management consulting company. Would like to have a clean and professional business card, based on the attached logo. The company is a strategy and management consulting company focusing on sustainable business modlels based on economic, social and environmental market opportunities. Preferably the logo should be included on both sides of the design.

Industry/Entity Type

Business

Contact Information for Business Card

Håvard Lilleby, CEO/Management consultant
havard.lilleby@quarvenpartners.example
Mob: +47 948 26 317
Office: Vikfjell gate 14, pb 312 sentrum, N-0172 Oslo Norway

Requirements
Must have
• Include attached logo
Nice to have
• Would like to have the logo on both sides
Should not have
• Many colours.

```html
<!DOCTYPE html>
<html lang="en">
<head>
<meta charset="utf-8">
<title>Quarven business card</title>
<link rel="stylesheet" href="https://fonts.googleapis.com/css2?family=Nunito+Sans:wght@400;700;800&display=swap">
<style>
  :root {
    --bg: #2c2c2e;
    --card-dark: #1c1c1d;
    --brand-yellow: #f0d21c;
    --ink: #1a1a1a;
    --white: #f4f4f4;
    --muted: #d6d6d6;
    --band: #ececec;
  }
  * { margin: 0; padding: 0; box-sizing: border-box; }
  html, body {
    width: 1200px; height: 960px; overflow: hidden;
    background: var(--bg);
    font-family: "Nunito Sans", sans-serif;
  }
  .canvas {
    position: relative; width: 1200px; height: 960px;
  }
  .card {
    position: absolute; left: 250px;
    width: 700px; height: 420px;
    border-radius: 4px;
    overflow: hidden;
  }
  .card-front { top: 45px; background: var(--brand-yellow); }
  .card-back { top: 495px; background: var(--card-dark); }

  .front-wordmark {
    position: absolute; inset: 0;
    display: flex; align-items: center; justify-content: center;
    font-size: 110px; font-weight: 800; color: var(--ink);
    letter-spacing: -2px;
  }

  .back-wordmark {
    position: absolute; left: 44px; top: 118px;
    font-size: 60px; font-weight: 800; color: var(--white);
    letter-spacing: -1px;
  }
  .divider {
    position: absolute; left: 305px; top: 110px;
    width: 1px; height: 150px; background: #8a8a8a;
  }
  .contact {
    position: absolute; left: 325px; top: 112px;
    color: var(--muted); font-size: 18px; line-height: 1.3;
  }
  .contact-name {
    color: var(--brand-yellow); font-weight: 800;
    text-transform: uppercase; font-size: 20px;
  }
  .contact-title { text-transform: uppercase; font-size: 18px; margin-bottom: 8px; }
  .contact-line { white-space: nowrap; }

  .web-band {
    position: absolute; left: 0; top: 300px;
    width: 560px; height: 36px; background: var(--band);
    display: flex; align-items: center; padding-left: 44px;
    font-size: 17px; font-weight: 700; letter-spacing: 6px; color: var(--ink);
  }
  .accent-dot {
    position: absolute; right: 38px; bottom: 34px;
    width: 38px; height: 38px; border-radius: 50%;
    background: var(--brand-yellow);
  }
</style>
</head>
<body>
<main class="canvas">
  <section class="card card-front" aria-label="Card front">
    <div class="front-wordmark">Quarven</div>
  </section>

  <section class="card card-back" aria-label="Card back">
    <div class="back-wordmark">Quarven</div>
    <div class="divider"></div>
    <div class="contact">
      <div class="contact-name">Håvard Lilleby</div>
      <div class="contact-title">CEO/Management<br>Consultant</div>
      <div class="contact-line">Vikfjell gate 14,</div>
      <div class="contact-line">pb 312 sentrum, N-0172 Oslo Norway</div>
      <div class="contact-line">M. +47 948 26 317</div>
      <div class="contact-line">havard.lilleby@quarvenpartners.example</div>
    </div>
    <div class="web-band">www.quarvenpartners.example</div>
    <div class="accent-dot"></div>
  </section>
</main>
</body>
</html>
```